Web Design Concept for new social network

We need a fresh, vibrant, clean web design layout for a new social network that we are trying to put together.
The site itself will be stuffed with little jquery/css tricks to enable a better/better looking UI (this is where you come in).
Imagine you were re-imagining Chatterbox.. How would you have designed it? The new site, will have a lot of similar functions to CB, and then a few more.
I will need a great looking sign in page in addition to;
The main page will need to have the following elements;
- Profile header.
Profile picture and tabbed area for various pieces of meta data contact details, preferences etc
- A Post Wall (like the wall on CB, but its crossed with a quillet-esque global search/post). People can respond to not only the original message, but can reply to each individual reply.
Instead of LIKE, there will need to be a positive/negative/neutral style option (feel free to get creative with naming). The background of each post will reflect the average rating (pos/nuetral/neg) of the post itself.. so if 100 people click pos, 50 neutral and 1 negative, the bg will mainly be the positive colour).
The feed will include messages by default from many sources (chatterbox/quillet/worked up) there should be somewhere that these can be switched on and off...
Somewhere to post a message - again by default it will post to all networks, but should be able to switch off.
Images/Videos/Text can all be posted to the wall (if you can think of a better name than wall - please use that!)
- Notifications; rather than having them in a drop down menu like cb, i want them to be in a hidden div (one div for each type) that slides open to reveal the notifications.. The default will be that the divs are closed so if there is a new notification there will be a need for something to appear on the screen that the user can click. We will need 3 notification types.
- Calendar; collapsable
- Options for today/this week/month views etc
- Menu system to navigate to other screens.
This should be able to show available things like groups/pages/events (again feel free to rename).
The screens themselves should appear to be stacked (like stacked tiles).
- Search; there should be a search bar somewhere with various options being available.
- Modal popup. I will be using modal popups across the site so will want a consistant feel (should be able to display photos/videos etc)
I will upload some files over the next few days to support the above, but am really looking for your creativity here.
Sites I really like the style of:
- the NEW roomnest (check it out.. its awesome).
- plumb
- quillet
I want a really clean interface, modern.. splashes of colour are fine (but only where it will enhance).
Updates
I have added a file to the uploads that gives an idea of how the notifications should be revealed.. Please do not read too much into any styling... i created the pdf just to show how i expect the notifications to be revealed, and that I expect there to be multiple notification types.
Although I deliberately didnt request adverts to be shown in the brief, i also didnt explicitly state that they shouldnt be! The site will NOT feature adverts so please do not show them on the design. Id much rather that the space be used to improve layout.
Target Market(s)
18 to 40 - again, think chatterbox/quillet/workedup
Industry/Entity Type
Events
Look and feel

```html
<!DOCTYPE html>
<html lang="en">
<head>
<meta charset="utf-8">
<title>Hubbub – Profile</title>
<link href="https://fonts.googleapis.com/css2?family=Source+Sans+3:wght@400;600;700&display=swap" rel="stylesheet">
<style>
:root{
  --bg:#efefef;--card:#fff;--line:#e2e2e2;--tab:#f3f3f3;
  --text:#333;--muted:#9a9a9a;--green:#8cb829;--green-dk:#6f9a17;
  --blue:#2d6fbf;--dark:#2b2b2b;--sel:#1f5fd6;
  --photo1:#b7a08a;--photo2:#5b5149;--photo3:#c9b7a4;
}
*{box-sizing:border-box;margin:0;padding:0}
html,body{width:852px;height:1200px;overflow:hidden}
body{background:var(--bg);font-family:"Source Sans 3",sans-serif;color:var(--text);font-size:11px;position:relative}
a{color:var(--blue);text-decoration:none}
.abs{position:absolute}
.header{left:0;top:0;width:852px;height:50px;background:#fff;border-bottom:1px solid var(--line)}
.brand{left:64px;top:18px;font-size:13px;font-weight:700;color:var(--dark);display:flex;align-items:center;gap:5px;white-space:nowrap}
.brand i{width:9px;height:9px;background:var(--green);display:block}
.nav{left:130px;top:21px;display:flex;gap:16px;font-size:11px;white-space:nowrap}
.nav a{color:var(--green)}.nav a:first-child{color:var(--text)}
.search{left:535px;top:21px;width:175px;height:17px;border:1px solid #ddd;border-radius:2px;color:#aaa;font-size:9.5px;padding:2px 10px;background:#fafafa}
.search svg{position:absolute;right:6px;top:3px}
.gear{left:733px;top:18px}
.card{background:var(--card);border:1px solid var(--line)}
.tabs{display:flex;height:30px;background:var(--tab);border-bottom:1px solid var(--line)}
.tabs span{padding:0 13px;line-height:30px;font-size:11px;border-right:1px solid var(--line)}
.tabs span.on{background:#fff}
.ph{background:linear-gradient(160deg,var(--photo3),var(--photo1) 50%,var(--photo2))}
.profile{left:78px;top:66px;width:468px;height:270px}
.profile .pic{left:11px;top:41px;width:133px;height:150px}
.name{left:162px;top:38px;font-size:17px}
.sub{left:162px;top:58px;color:var(--muted);font-size:10px;line-height:14px}
.sub b{font-weight:400;color:#555}
.edit{left:424px;top:38px;background:var(--green);color:#fff;font-weight:700;font-size:8.5px;padding:3px 8px;border-radius:3px;white-space:nowrap}
.facts{left:162px;top:110px;display:grid;grid-template-columns:48px 97px 74px 80px;row-gap:13px;font-size:11px;white-space:nowrap}
.facts .v{color:var(--blue)}
.about{left:14px;top:202px;width:445px}
.about h3{font-weight:400;font-size:13px;margin-bottom:4px}
.lorem{color:var(--muted);font-size:9.5px;line-height:13.5px}
.feed{left:78px;top:348px;width:468px;height:808px}
.share{margin:5px;height:50px;border:1px solid #ddd;border-radius:3px;color:#aaa;font-size:10px;padding:10px 12px}
.wall{left:78px;top:442px;width:469px;height:35px;background:var(--dark);color:#fff;display:flex;align-items:center;padding:0 16px;font-size:13px}
.wall .f{margin-left:auto;font-size:9.5px;font-weight:700}
.wall .f u{font-weight:400;color:#ccc;margin:0 10px}
.post-h{height:34px;background:#f1f1f1;border-bottom:1px solid var(--line);display:flex;align-items:center;padding:0 16px;gap:16px;color:var(--blue);font-size:12px}
.av{width:26px;height:26px;background:linear-gradient(160deg,#d8c2ae,#6d5a4b)}
.actions{display:flex;align-items:center;gap:6px;font-size:7.5px;color:var(--blue);padding:0 16px;white-space:nowrap}
.dot{width:9px;height:9px;border-radius:50%}
.actions .t{margin-left:auto;color:#bbb}
.cbox{margin:0 8px 0 9px;height:27px;border:1px solid #ddd;border-radius:2px;color:#aaa;font-size:10px;padding:6px 12px}
.reply{display:flex;gap:8px;padding:0 8px 0 12px;position:relative;font-size:8.5px;line-height:12px}
.reply .av{width:34px;height:34px;flex:none}
.reply b{color:var(--blue);font-weight:400}
.reply small{display:block;color:#bbb;font-size:7px}
.reply em{position:absolute;right:16px;bottom:2px;font-style:normal;color:var(--blue);font-size:7.5px}
.side{left:553px;width:221px}
.side-h{height:30px;background:var(--tab);border-bottom:1px solid var(--line);font-size:12px;padding:0 13px;line-height:30px}
.tree{font-size:11px;padding-left:10px;line-height:21px}
.tree .on{background:var(--green);color:#fff;margin-left:-10px;padding-left:10px;height:18px;line-height:18px}
.ntf{display:flex;gap:10px;padding:5px 13px;background:#f7f7f7;margin-bottom:4px;height:46px}
.ntf .av{width:38px;height:38px;flex:none}
.ntf p{font-size:11px;line-height:12px}
.ntf small{display:block;color:var(--muted);font-size:7.5px;line-height:9.5px;margin-top:3px}
.more{text-align:right;font-size:7px;color:var(--blue);padding-right:10px}
.act{display:flex;gap:12px;padding:4px 10px;height:44px;border-bottom:4px solid #f4f4f4}
.act .ic{width:38px;height:38px;flex:none;border-radius:4px}
.act p{font-size:11px;padding-top:4px}
.act small{display:block;color:var(--muted);font-size:7.5px;margin-top:6px}
.cal{top:625px;height:197px;border:1px solid #ccc;background:#fff}
.cal-h{height:29px;background:var(--dark);color:#fff;display:flex;justify-content:space-between;align-items:center;padding:0 12px;font-size:12px}
.cal-g{display:grid;grid-template-columns:repeat(7,1fr)}
.cal-g .d{font-size:7px;color:#555;text-align:center;height:20px;line-height:22px}
.cal-g span{height:29px;border-right:1px solid #e4e4e4;border-top:1px solid #e4e4e4;text-align:center;line-height:28px;font-size:8.5px;font-weight:700;color:#333;background:#fcfcfc}
.cal-g span.o{color:#aaa;font-weight:400}
.cal-g span.s{background:var(--sel);color:#fff;outline:1px solid #0d3f9c}
.collapse{left:649px;top:822px;width:29px;height:16px;background:var(--dark);border-radius:0 0 3px 3px}
.sugg{top:846px;height:178px}
.people{display:flex;justify-content:space-around;padding:6px 4px 0;text-align:center}
.people .pic{width:59px;height:60px;margin:0 auto}
.people p{font-size:11.5px;margin-top:3px}
.people small{display:block;font-size:6.5px;color:#aaa}
.btn{display:inline-block;margin-top:4px;background:var(--green);color:#fff;font-size:7.5px;font-weight:700;padding:3px 7px;border-radius:2px;border:1px solid var(--green-dk);white-space:nowrap}
.footer{left:0;top:1168px;width:852px;height:32px;background:#fff;border-top:1px solid var(--line);font-size:9px;display:flex;align-items:center;padding:0 80px 0 86px}
.footer nav{margin-left:auto;display:flex;gap:18px}
</style>
</head>
<body>
<header class="header abs">
  <div class="brand abs"><i></i>Hubbub</div>
  <nav class="nav abs"><a>Home</a><a>Profile</a><a>Friends</a><a>Groups</a><a>News</a><a>More</a></nav>
  <div class="search abs">Search anything
    <svg width="16" height="10" viewBox="0 0 16 10"><circle cx="5" cy="4" r="3" fill="none" stroke="#888"/><path d="M3 6 1 9M12 4h4l-2 2z" stroke="#888" fill="#888"/></svg></div>
  <svg class="gear abs" width="30" height="22" viewBox="0 0 30 22"><circle cx="10" cy="11" r="7" fill="none" stroke="#777" stroke-width="3" stroke-dasharray="3 2"/><circle cx="10" cy="11" r="4" fill="none" stroke="#777" stroke-width="2"/><path d="M22 10h5l-2.5 3z" fill="#777"/></svg>
</header>

<section class="profile card abs">
  <div class="tabs"><span>Contact</span><span>Details</span><span>Preferences</span><span>Pages</span><span>Mobiles</span></div>
  <div class="pic ph abs" role="img" aria-label="Profile photo of the member"></div>
  <div class="name abs">Anonymous</div>
  <div class="sub abs">IT Professional<br><b>From</b> &nbsp; &nbsp;: Chicago, United States<br><b>Lives in :</b> Quebec, Canada</div>
  <div class="edit abs">Edit ✎</div>
  <div class="facts abs">
    <span>Status</span><span class="v">Single</span><span>Latest Activity</span><span class="v">Sep 16, 2012</span>
    <span>Birthday</span><span class="v">25 Sep, 1975</span><span>Date Joined</span><span class="v">Aug 22, 2012</span>
    <span>Friends</span><span class="v">(125)</span><span>Education</span><span class="v">B.Tech</span>
  </div>
  <div class="about abs"><h3>About me.</h3>
    <p class="lorem">Lorem ipsum dolor sit amet, consectetuer adipiscing elit, sed diam nonummy nibh euismod tincidunt ut laoreet dolore magna aliquam erat volutpat. Ut wisi enim ad minim veniam, quis nostrud exerci tation ullamcorper suscipit lobortis nisl ut aliquip ex ea commodo consequat. Duis autem vel eum iriure dolor in</p></div>
</section>

<section class="feed card abs">
  <div class="tabs"><span class="on">Status</span><span>Photos</span><span>Videos</span><span>Events</span></div>
  <div class="share">Share any Update</div>

  <article class="abs" style="left:0;top:141px;width:466px">
    <div class="post-h"><div class="av" role="img" aria-label="Author avatar"></div>Lorem ipsum dolor sit. (Video)</div>
    <div style="display:flex;gap:28px;padding:10px 8px 0 12px;height:100px">
      <div class="ph" style="width:127px;height:78px;flex:none" role="img" aria-label="Video still of a group of friends"></div>
      <div><p style="font-size:12px;margin:0 0 10px">Lorem ipsum dolor sit.</p>
      <p class="lorem">Lorem ipsum dolor sit amet, consectetuer adipiscing elit, sed diam nonummy nibh euismod tincidunt ut laoreet dolore magna aliquam erat volutpat. Ut wisi enim ad minim veniam,</p></div>
    </div>
    <div class="actions"><i class="dot" style="background:#5cb43a"></i><i class="dot" style="background:#e04646"></i><i class="dot" style="background:#5b8fd6"></i><span style="margin-left:22px">▭ Comment</span><span style="margin-left:8px">▣ Share</span><span class="t">15 minuts ago</span></div>
    <div class="cbox" style="margin-top:17px">Write a comment...</div>
  </article>

  <article class="abs" style="left:0;top:356px;width:466px">
    <div class="post-h"><div class="av" role="img" aria-label="Author avatar"></div>Lorem ipsum dolor sit. (Photo Album)</div>
    <div style="display:flex;gap:20px;padding:8px 8px 0 12px">
      <div class="ph" style="width:149px;height:115px;flex:none" role="img" aria-label="Portrait of Daniel Harlow in a suit"></div>
      <div style="padding-top:4px"><p style="font-size:12px;margin:0 0 8px">Daniel Harlow (Album)</p>
      <p class="lorem">Lorem ipsum dolor sit amet, consectetuer adipiscing elit, sed diam nonummy nibh euismod tincidunt ut laoreet dolore magna aliquam erat volutpat. Ut wisi enim ad minim veniam,</p>
      <p class="lorem" style="margin-top:12px">quis nostrud exerci tation ullamcorper suscipit lobortis nisl ut aliquip ex ea commodo consequat.</p></div>
    </div>
    <div style="display:flex;gap:8px;padding:6px 12px 0" role="img" aria-label="Album thumbnails">
      <div class="ph" style="width:72px;height:77px"></div><div class="ph" style="width:71px;height:77px"></div><div class="ph" style="width:90px;height:77px"></div><div class="ph" style="width:90px;height:77px"></div><div class="ph" style="width:86px;height:77px"></div>
    </div>
    <div class="actions" style="margin-top:22px"><i class="dot" style="background:#5cb43a"></i><i class="dot" style="background:#e04646"></i><i class="dot" style="background:#5b8fd6"></i><span style="margin-left:22px">▭ Comment</span><span style="margin-left:8px">▣ Share</span><span class="t">15 minuts ago</span></div>
    <div class="reply" style="margin-top:14px"><div class="av" role="img" aria-label="Commenter avatar"></div><div><b>Anonymous</b> Quis nostrud exerci tation ullamcorper suscipit lobortis nisl ut aliquip ex el eum iriure dolor in hendrerit in vulputate velit esse m<small>15 minuts ago</small></div><em>↩ Reply</em></div>
    <div style="border-top:1px solid #eee;margin:7px 0"></div>
    <div class="reply"><div class="av" role="img" aria-label="Commenter avatar"></div><div><b>Anonymous</b> Quis nostrud exerci tation ullamcorper suscipit lobortis nisl ut aliquip ex el eum iriure dolor in hendrerit in vulputate velit esse m<small>15 minuts ago</small></div><em>↩ Reply</em></div>
    <div class="cbox" style="margin-top:4px">Write a comment...</div>
  </article>
  <svg class="abs" style="left:222px;top:784px" width="26" height="18" viewBox="0 0 26 18"><rect x="0" y="6" width="4" height="10" fill="#ddd"/><rect x="7" y="4" width="4" height="12" fill="#ccc"/><rect x="14" y="2" width="4" height="14" fill="#bbb"/><rect x="21" y="0" width="4" height="16" fill="#aaa"/></svg>
</section>
<div class="wall abs">Wall<span class="f">Filter : <u>Last Week</u>▾</span></div>

<aside class="side card abs" style="top:66px;height:270px">
  <div class="side-h">Notifications <span style="display:inline-block;width:10px;height:8px;background:var(--green);border-radius:2px"></span></div>
  <div class="tree" style="margin-top:4px"><div>‣ Apps</div><div>‣ Pages</div><div class="on">▾ Friends</div></div>
  <div style="margin-top:6px">
    <div class="ntf"><div class="av" role="img" aria-label="Friend avatar"></div><p>Anonymous<small>ABC accept your friendship request<br>Send message to her</small></p></div>
    <div class="ntf"><div class="av" role="img" aria-label="Friend avatar"></div><p>Anonymous<small>Your friend request has been approved.<br>Send message to her</small></p></div>
    <div class="ntf"><div class="av" role="img" aria-label="Friend avatar"></div><p>Anonymous<small>Your friend request has been approved.<br>Send message to her</small></p></div>
  </div>
  <div class="more">View all</div>
</aside>

<aside class="side card abs" style="top:346px;height:272px">
  <div class="side-h">Recent Activites</div>
  <div style="padding-top:10px">
    <div class="act"><div class="ic ph" role="img" aria-label="Music artist photo"></div><p>Anonymous<small>Anonymous is listening <a>Mara Voss</a></small></p></div>
    <div class="act"><div class="ic" style="background:#eee"></div><p>Anonymous<small>Anonymous like <a>Veltro Motors</a></small></p></div>
    <div class="act"><div class="ic" style="background:#e6efe8"></div><p>Anonymous<small>Anonymous like <a>Brewline Coffee</a></small></p></div>
    <div class="act" style="border:0"><div class="ic" style="background:#f6e4e2"></div><p>Anonymous<small>Anonymous start playing <a>Cross Birds</a></small></p></div>
  </div>
  <div class="more" style="margin-top:4px">More Recent Activites</div>
</aside>

<aside class="side cal abs">
  <div class="cal-h"><span>‹</span>12 January 2012<span>›</span></div>
  <div class="cal-g">
    <div class="d">MON</div><div class="d">TUE</div><div class="d">WED</div><div class="d">THU</div><div class="d">FRI</div><div class="d">SAT</div><div class="d">SUN</div>
    <span class="o">30</span><span>1</span><span>2</span><span>3</span><span>4</span><span>5</span><span>6</span>
    <span>7</span><span>8</span><span>9</span><span>10</span><span>11</span><span class="s">12</span><span>13</span>
    <span>14</span><span>15</span><span>16</span><span>17</span><span>18</span><span>19</span><span>20</span>
    <span>21</span><span>22</span><span>23</span><span>24</span><span>25</span><span>26</span><span>27</span>
    <span>28</span><span>29</span><span>30</span><span>31</span><span class="o">1</span><span class="o">2</span><span class="o">3</span>
  </div>
</aside>
<div class="collapse abs"></div>

<aside class="side sugg card abs">
  <div class="side-h" style="font-size:13px">Suggestion</div>
  <div class="people">
    <div><div class="pic ph" role="img" aria-label="Suggested member photo"></div><p>Lorem</p><small>Send Message</small><span class="btn">View Profile</span></div>
    <div><div class="pic ph" role="img" aria-label="Suggested member photo"></div><p>Ipsum</p><small>Send Message</small><span class="btn">View Profile</span></div>
    <div><div class="pic ph" role="img" aria-label="Suggested member photo"></div><p>Dolor</p><small>Send Message</small><span class="btn">View Profile</span></div>
  </div>
  <div class="more" style="margin-top:18px">Show All</div>
</aside>

<footer class="footer abs">© 2012 Hubbub. All Rights Reserved
  <nav><span>About</span><span>Services</span><span>Portfolio</span><span>Blog</span><span>Contact</span></nav>
</footer>
</body>
</html>
```